Graphic Design for 2026 PLEVCO Summit – 4:3 Ratio Event Image

The Harbor Guild of Livery Makers and Resellers (PLEVCO) is seeking a high-quality, professional graphic to serve as the primary visual template for our 2026 PLEVCO Summit & Showcase. This image will be used across digital, print, and on-site event materials. We need a visually striking, industry-relevant design that reflects the uniform, image apparel, and workwear industry and captures the spirit of innovation, networking, and global connection that defines our annual convention.

Key Details:
Event Name: 2026 PLEVCO Summit & Showcase

Audience: Uniform manufacturers, distributors, and suppliers serving public safety, hospitality, healthcare, corporate, and industrial markets.

Purpose of Image:

Serve as the main branding graphic for the convention.

Be adaptable for use on our website, social media, email campaigns, signage, and printed materials.

Provide a modern, professional, future-focused look appealing to business decision-makers in the uniform and workwear sector.

Design Requirements:
Format: Layered file delivery (Adobe Illustrator or Photoshop).

If Photoshop, final file must be minimum 2500px wide for high-quality print output.

Aspect Ratio: 4:3 (landscape).

Style:

Clean, professional, and corporate.

Forward-looking, innovative feel (not dated or generic).

Should represent the diverse industries where uniforms are worn (public safety, healthcare, hospitality, industrial, corporate office).

Abstract or conceptual elements (e.g., flowing fabric, silhouettes of professionals, global connections) are welcome. Avoid clip-art or overly literal graphics.

Color Palette: Prefer use of PLEVCO’s primary brand colors where possible:

Blue: #204295

Red: #EC1F25
Designers may incorporate complementary colors to enhance the look, but these two should be prominent.

Deliverables:
Main design file in Illustrator (.AI) or Photoshop (.PSD), layered and editable.

High-resolution exported version for immediate use.

Adaptable design suitable for other sizes and formats in future.

Inspiration:
We want a bold, memorable image that conveys:

The professionalism and scale of the uniform industry.

Innovation, progress, and networking.

Global reach and cross-industry connections fostered by PLEVCO’s annual convention.

Usage Rights:
PLEVCO will retain full rights to the final chosen design for unlimited future use across digital and print channels.

Attached is a rough concept I created. I’m not satisfied with it, but it shows the basic layout idea. I’d like you to take the concept to a much more professional, polished level, incorporating our brand colors (Blue #204295, Red #EC1F25) and a modern, corporate feel.

Requirements
Must have
• Include this text: Currents of Change: The Flow of Ideas, People, and Possibility PLEVCO 2026 SUMMIT Uniform and Workwear Professionals

```html
<!DOCTYPE html>
<html lang="en">
<head>
<meta charset="utf-8">
<title>2026 PLEVCO Summit & Showcase</title>
<link href="https://fonts.googleapis.com/css2?family=Manrope:wght@400;500;700;800&display=swap" rel="stylesheet">
<style>
  :root {
    --navy: #1b2a5c;
    --brand-blue: #204295;
    --blue: #2f63e6;
    --red: #ec1f25;
    --body: #5a6275;
    --white: #ffffff;
    --photo-light: #cdbda4;
    --photo-mid: #8a7560;
    --photo-dark: #3a3438;
    --photo-crowd: #4a4046;
  }
  * { margin: 0; padding: 0; box-sizing: border-box; }
  html, body { width: 1200px; height: 900px; overflow: hidden; background: var(--white); }
  body { font-family: "Manrope", sans-serif; position: relative; }

  .hero-photo { position: absolute; left: 0; top: 0; width: 1200px; height: 540px; }

  .event-banner {
    position: absolute; left: 71px; top: 56px; width: 640px;
    color: var(--white);
  }
  .event-banner__eyebrow {
    display: inline-block; background: var(--red);
    font-weight: 800; font-size: 14px; letter-spacing: 2.4px;
    padding: 7px 14px; margin-bottom: 18px;
  }
  .event-banner__title {
    font-weight: 800; font-size: 36px; line-height: 42px; letter-spacing: -0.3px;
  }
  .event-banner__audience {
    margin-top: 14px; font-weight: 500; font-size: 17px; letter-spacing: 0.4px;
    opacity: 0.92;
  }

  .brand-block {
    position: absolute; left: 71px; top: 378px;
    width: 120px; height: 162px; background: var(--red);
  }

  .headline {
    position: absolute; left: 225px; top: 386px;
    color: var(--navy); font-weight: 800; font-size: 52.5px;
    line-height: 48px; letter-spacing: -0.5px;
  }
  .tagline {
    position: absolute; left: 225px; top: 497px;
    color: var(--navy); font-weight: 400; font-size: 19.5px;
  }

  .column { position: absolute; top: 606px; }
  .column--attendees { left: 79px; width: 500px; }
  .column--exhibitors { left: 604px; width: 560px; }
  .column__title {
    color: var(--navy); font-weight: 700; font-size: 20px;
    letter-spacing: 0.3px; margin-bottom: 30px;
  }
  .column__lead {
    display: flex; align-items: center; gap: 18px;
    color: var(--body); font-weight: 500; font-size: 16.5px; margin-bottom: 16px;
  }
  .column__lead svg { flex: none; }
  .column__text {
    padding-left: 30px; color: var(--body); font-weight: 400;
    font-size: 16px; line-height: 27.6px;
  }
  .column--attendees .column__text { width: 482px; }
  .column--exhibitors .column__text { width: 530px; }
</style>
</head>
<body>
  <svg class="hero-photo" viewBox="0 0 1200 540" role="img" aria-label="Photo of a packed convention ballroom with attendees at round tables listening to a speaker at a podium">
    <defs>
      <linearGradient id="room" x1="0" y1="0" x2="0" y2="1">
        <stop offset="0" stop-color="var(--photo-light)"/>
        <stop offset="0.38" stop-color="var(--photo-mid)"/>
        <stop offset="0.62" stop-color="var(--photo-crowd)"/>
        <stop offset="1" stop-color="var(--photo-dark)"/>
      </linearGradient>
      <linearGradient id="scrim" x1="0" y1="0" x2="1" y2="0">
        <stop offset="0" stop-color="#1b2a5c" stop-opacity="0.82"/>
        <stop offset="0.55" stop-color="#204295" stop-opacity="0.35"/>
        <stop offset="1" stop-color="#204295" stop-opacity="0"/>
      </linearGradient>
    </defs>
    <path d="M0 0 H1200 V532 C1185 420 1100 312 985 306 H0 Z" fill="url(#room)"/>
    <path d="M0 0 H1200 V532 C1185 420 1100 312 985 306 H0 Z" fill="url(#scrim)"/>
  </svg>

  <header class="event-banner">
    <p class="event-banner__eyebrow">PLEVCO 2026 SUMMIT</p>
    <h2 class="event-banner__title">Currents of Change: The Flow of Ideas, People, and Possibility</h2>
    <p class="event-banner__audience">Uniform and Workwear Professionals</p>
  </header>

  <div class="brand-block" aria-hidden="true"></div>

  <h1 class="headline">Where the Uniform Industry<br>Connects, Innovates, and Grows</h1>
  <p class="tagline">The essential gathering for apparel professionals, suppliers, and decision-makers.</p>

  <section class="column column--attendees">
    <h2 class="column__title">ATTENDEES</h2>
    <p class="column__lead">
      <svg width="12" height="12" viewBox="0 0 12 12" aria-hidden="true"><path d="M0 12 A12 12 0 0 1 12 0 V12 Z" fill="var(--blue)"/></svg>
      400+ Uniform, Image Apparel &amp; Workwear Professionals
    </p>
    <p class="column__text">The annual PLEVCO Summit and Showcase is attended by executives, sales leaders, merchandisers, designers, business owners, sourcing specialists, and other key professionals in the uniform and image apparel industry.</p>
  </section>

  <section class="column column--exhibitors">
    <h2 class="column__title">EXHIBITORS</h2>
    <p class="column__lead">
      <svg width="12" height="12" viewBox="0 0 12 12" aria-hidden="true"><path d="M0 12 A12 12 0 0 1 12 0 V12 Z" fill="var(--blue)"/></svg>
      75+ Uniform, Workwear, Fabric, Accessory, and Factory Suppliers
    </p>
    <p class="column__text">Booth space is at a premium for this highly targeted convention, where leading uniform manufacturers, mills, production facilities, and associated service providers meet small and large distributors, dealers, and brands.</p>
  </section>
</body>
</html>
```